Bold & Clean Birch Harbor Stationary Design

Our company, Birch Harbor Advisory Partners needs a business card, letterhead, and envelope design that all also the formatting standards for quillpressdepot.com.

Envelope:
Safe Zone: 9.375" x 4"
Trim Size: 9.5" x 4.15"
Bleed Size: 11.125" 8.625"

Letterhead:
Safe Zone: 10.875" x 8.375"
Trim Size: 11" x 8.5"
Bleed Size: 11.125" x 8.625"

Our mailing address is:
7318 W Larkmoor Rd
Chicago, IL 60647

Please make sure the return address on the envelope is formatted correctly for mailing and the logo is not too large.

Please submit designs in word and PDF form.

Our current letterhead is attached.

We would also like a business card with our existing logo that will meet standards for formatting through Quill Press Depot (quillpressdepot.com).

These standards are:
Safe Zone: 3.375" x 1.875"
Trim Size: 3.5" x 2"
Bleed Size: 3.625" x 2.125"

The business card is going to be for Marcus Lindqvist, President/CEO of Birch Harbor Advisory Partners. Please include the Address, Telephone Number, Cell Phone Number, Fax Number, Email, and Website Address on the card, which are as follows:

7318 W Larkmoor Rd
Chicago, IL 60647

Tel: (773) 591-3072
Cell: (630) 287-6093
Fax: (63) 417-2058
Email: mjl@birchharboradvisory.com
Web: www.birchharboradvisory.com

Please make sure that we can easily change the name of the staff member and job position title ourselves as we will be having cards for individual employees in the future as well.

The back of the card should also have the Birch Harbor logo on it with our services listed:

Financial Planning | Tax | Solutions for Small Businesses

Industry/Entity Type

Accounting

Requirements
Must have
• envelope
• letterhead
• business card
• All meeting standards set out above.

```html
<!DOCTYPE html>
<html lang="en">
<head>
<meta charset="utf-8">
<title>Birch Harbor Advisory Partners – Stationery</title>
<link rel="stylesheet" href="https://fonts.googleapis.com/css2?family=Exo+2:wght@400;600;700&family=Arimo:wght@400;700&display=swap">
<style>
  :root{
    --navy:#1f2f63;
    --orange:#f25a29;
    --paper:#ffffff;
    --ground:#e8e9eb;
    --ink:#3a3a3a;
  }
  *{margin:0;padding:0;box-sizing:border-box}
  html,body{width:1200px;height:937px;overflow:hidden;background:var(--ground)}
  body{position:relative;font-family:"Arimo",Arial,sans-serif;color:var(--ink)}
  .sheet{position:absolute;background:var(--paper);overflow:hidden}
  .wave{position:absolute;left:0;bottom:0;width:100%;display:block}
  .brand{position:absolute;display:flex;align-items:center;color:var(--navy);font-family:"Exo 2",sans-serif;font-weight:700;line-height:1}
  .brand-dot{border-radius:50%;border:2px solid var(--navy);flex:none}
  .brand-name{display:flex;flex-direction:column}
  .brand-sub{letter-spacing:.2em;margin-top:.25em}
  .url{position:absolute;color:#fff;font-family:"Exo 2",sans-serif;letter-spacing:.18em;white-space:nowrap}

  /* letterhead */
  .letterhead{left:185px;top:68px;width:387px;height:542px}
  .letterhead .brand{left:20px;top:24px;font-size:19px}
  .letterhead .brand-dot{width:30px;height:30px;margin-right:8px}
  .letterhead .brand-sub{font-size:7px}
  .letter{position:absolute;left:37px;top:140px;width:300px;font-size:5.6px;line-height:1.45}
  .letter p{margin-bottom:9px}
  .letter .strong{font-weight:700}
  .signature{width:28px;height:14px;background:#d4d6db;border-radius:2px;margin:4px 0 6px}
  .letter-contact{position:absolute;right:18px;bottom:8px;color:#fff;font-size:5.6px;line-height:1.9;text-align:right}
  .letter-contact b{font-weight:700;font-size:6px}
  .ic{display:inline-block;width:5px;height:5px;border:1px solid #fff;border-radius:1px;margin-left:4px;vertical-align:-1px}
  .ic.round{border-radius:50%}

  /* folder */
  .folder{left:636px;top:41px;width:457px;height:575px}
  .folder .brand{left:62px;top:245px;font-size:38px}
  .folder .brand-dot{width:62px;height:62px;border-width:3px;margin-right:14px}
  .folder .brand-sub{font-size:12px}
  .folder .url{right:16px;bottom:10px;font-size:11.5px}

  /* business cards */
  .card{width:175px;height:99px;border-radius:6px}
  .card-front{left:46px;top:659px}
  .card-back{left:46px;top:784px}
  .card .brand{left:8px;top:12px;font-size:10px}
  .card .brand-dot{width:15px;height:15px;border-width:1.5px;margin-right:4px}
  .card .brand-sub{font-size:4px}
  .card-person{position:absolute;right:8px;top:9px;text-align:right;color:var(--navy);font-size:5.4px;line-height:1.3}
  .card-person b{font-size:6.2px;font-weight:700;letter-spacing:.02em}
  .card-contact{position:absolute;right:7px;bottom:4px;color:#fff;font-size:3.8px;line-height:1.45;text-align:right}
  .card-services{position:absolute;left:0;right:0;bottom:14px;text-align:center;color:var(--navy);font-size:5.2px;font-weight:700;white-space:nowrap}
  .card-services-rule{position:absolute;left:8px;right:8px;bottom:26px;height:1px;background:var(--orange)}

  /* envelope front */
  .envelope{left:266px;top:671px;width:437px;height:209px}
  .envelope .brand{left:16px;top:28px;font-size:21px}
  .envelope .brand-dot{width:34px;height:34px;margin-right:8px}
  .envelope .brand-sub{font-size:7px}
  .return-address{position:absolute;left:58px;top:72px;color:var(--navy);font-size:7px;line-height:1.4}
  .envelope .url{left:240px;bottom:12px;font-size:9px}

  /* envelope back */
  .envelope-back{left:737px;top:671px;width:431px;height:209px}
  .flap{position:absolute;left:0;top:0;width:100%;height:72px;background:var(--orange);border-radius:0 0 32px 32px}
  .envelope-back .url{left:0;right:0;top:28px;text-align:center;font-size:11px}
</style>
</head>
<body>

<!-- Letterhead -->
<section class="sheet letterhead">
  <div class="brand">
    <span class="brand-dot"></span>
    <span class="brand-name">Birch Harbor<span class="brand-sub">ADVISORY PARTNERS</span></span>
  </div>
  <div class="letter">
    <p>July 2, 2012</p>
    <p><span class="strong">Dear Client,</span><br>7318 W Larkmoor Rd, Chicago, IL 60647</p>
    <p>Thank you for choosing our team to guide your financial planning. We review every plan with care and keep your goals at the center of each decision we make together this year.</p>
    <p>Our advisors will contact you soon to arrange a review of your tax position.</p>
    <p>We look forward to supporting your household and your small business with clear, steady advice in every season ahead.</p>
    <p style="margin-bottom:2px">Best Regards,</p>
    <div class="signature" role="img" aria-label="Handwritten signature"></div>
    <p><span class="strong">Helena Varga</span><br>Director<br><br>7318 W Larkmoor Rd, Chicago, IL 60647</p>
  </div>
  <svg class="wave" viewBox="0 0 400 110" height="110" preserveAspectRatio="none" aria-hidden="true">
    <path fill="var(--navy)" d="M0,68 C130,74 225,42 305,16 C345,4 380,0 400,0 L400,110 L0,110Z"/>
    <path fill="none" stroke="#fff" stroke-width="2" d="M0,79 C130,84 228,52 312,25 C352,13 384,9 400,9"/>
    <path fill="var(--orange)" d="M0,86 C130,90 232,60 320,33 C358,22 388,19 400,19 L400,110 L0,110Z"/>
  </svg>
  <div class="letter-contact">
    <b>7318 W Larkmoor Rd</b><br><b>Chicago, IL 60647</b><br>
    (773) 591-3072<span class="ic"></span><br>
    (630) 287-6093<span class="ic"></span><br>
    (63) 417-2058<span class="ic"></span><br>
    mjl@birchharboradvisory.com<span class="ic"></span><br>
    www.birchharboradvisory.com<span class="ic round"></span>
  </div>
</section>

<!-- Presentation folder -->
<section class="sheet folder">
  <div class="brand">
    <span class="brand-dot"></span>
    <span class="brand-name">Birch Harbor<span class="brand-sub">ADVISORY PARTNERS</span></span>
  </div>
  <svg class="wave" viewBox="0 0 400 140" height="160" preserveAspectRatio="none" aria-hidden="true">
    <path fill="var(--navy)" d="M0,95 C120,100 200,60 290,22 C340,4 380,0 400,0 L400,140 L0,140Z"/>
    <path fill="none" stroke="#fff" stroke-width="2.5" d="M0,108 C120,112 205,72 300,34 C348,17 385,12 400,12"/>
    <path fill="var(--orange)" d="M0,116 C125,118 212,82 308,44 C352,29 388,25 400,25 L400,140 L0,140Z"/>
  </svg>
  <div class="url">www.birchharboradvisory.com</div>
</section>

<!-- Business card front -->
<section class="sheet card card-front">
  <div class="brand">
    <span class="brand-dot"></span>
    <span class="brand-name">Birch Harbor<span class="brand-sub">ADVISORY PARTNERS</span></span>
  </div>
  <div class="card-person"><b>MARCUS LINDQVIST</b><br>President/CEO</div>
  <svg class="wave" viewBox="0 0 400 160" height="70" preserveAspectRatio="none" aria-hidden="true">
    <path fill="var(--navy)" d="M0,120 C100,122 190,70 270,30 C320,8 370,0 400,0 L400,160 L0,160Z"/>
    <path fill="none" stroke="#fff" stroke-width="3" d="M0,133 C105,134 198,84 282,44 C330,22 375,15 400,15"/>
    <path fill="var(--orange)" d="M0,142 C110,142 205,96 292,56 C338,36 380,30 400,30 L400,160 L0,160Z"/>
  </svg>
  <div class="card-contact">
    7318 W Larkmoor Rd<br>Chicago, IL 60647<br>
    Tel: (773) 591-3072<br>Cell: (630) 287-6093<br>Fax: (63) 417-2058<br>
    mjl@birchharboradvisory.com<br>www.birchharboradvisory.com
  </div>
</section>

<!-- Business card back -->
<section class="sheet card card-back">
  <div class="brand">
    <span class="brand-dot"></span>
    <span class="brand-name">Birch Harbor<span class="brand-sub">ADVISORY PARTNERS</span></span>
  </div>
  <div class="card-services-rule"></div>
  <div class="card-services">Financial Planning | Tax | Solutions for Small Businesses</div>
</section>

<!-- Envelope front -->
<section class="sheet envelope">
  <div class="brand">
    <span class="brand-dot"></span>
    <span class="brand-name">Birch Harbor<span class="brand-sub">ADVISORY PARTNERS</span></span>
  </div>
  <address class="return-address" style="font-style:normal">7318 W Larkmoor Rd<br>Chicago, IL 60647</address>
  <svg class="wave" viewBox="0 0 400 110" height="112" preserveAspectRatio="none" aria-hidden="true">
    <path fill="var(--navy)" d="M0,65 C110,66 190,38 270,15 C320,3 370,0 400,0 L400,110 L0,110Z"/>
    <path fill="none" stroke="#fff" stroke-width="2" d="M0,75 C115,76 198,48 282,25 C330,13 376,10 400,10"/>
    <path fill="var(--orange)" d="M0,82 C120,82 205,56 292,33 C338,22 382,19 400,19 L400,110 L0,110Z"/>
  </svg>
  <div class="url">www.birchharboradvisory.com</div>
</section>

<!-- Envelope back -->
<section class="sheet envelope-back">
  <div class="flap"></div>
  <div class="url">www.birchharboradvisory.com</div>
</section>

</body>
</html>
```